Mailchimp email (Monthly performance report design)

We need someone to code an HTML file as this will be used to import the template to Mailchimp.

We need a slick and professionally designed email layout to be used via Mailchimp. The target audience is sophisticated investors.

We have attached our current email template that is being used (File name: Capture 1). We have also added an inspiration piece (File name: Capture). The content needs to be transferred to the new template. We have 3 funds and we want them to be somehow presented in 3 columns. The pictures need to be professional business or nature bleu theme. We have also uploaded a template to provide you with guidance on how the layout should be. You are free to use your imagination and make changes as deemed.

This is our website: https://www.tarnwellholdings.com/. The color theme of the template should match the website.

The pictures need to be professional business or nature bleu theme.

Coding

```html
<!DOCTYPE html>
<html lang="en">
<head>
<meta charset="utf-8">
<title>Tarnwell Holdings – Monthly Report Email Templates</title>
<link href="https://fonts.googleapis.com/css2?family=Montserrat:wght@400;500;600;700;800;900&display=swap" rel="stylesheet">
<style>
  :root{
    --stage:#b9b9b9;
    --navy:#1f3854;
    --ice:#eef6fd;
    --white:#ffffff;
    --ink:#111111;
    --frame:#2b9bf0;
    --lime:#a6e86a;
    --bar:#c5c5c5;
  }
  *{margin:0;padding:0;box-sizing:border-box}
  html,body{width:1039px;height:1200px;overflow:hidden}
  body{
    position:relative;
    font-family:"Montserrat",sans-serif;
    color:var(--ink);
    background:radial-gradient(ellipse at center,#d6d6d6 0%,var(--stage) 55%,#a9a9a9 100%);
  }
  .variant-title{
    position:absolute;top:81px;width:416px;text-align:center;
    font-size:17px;font-weight:800;letter-spacing:.3px;color:#1c1c1c;
  }
  .email{
    position:absolute;top:145px;width:416px;height:956px;background:var(--white);
    box-shadow:0 4px 18px rgba(0,0,0,.18);overflow:hidden;
  }
  .email--one{left:83px}
  .email--two{left:540px}

  /* header */
  .masthead{position:absolute;top:0;left:0;width:416px;height:50px;background:var(--navy)}
  .brand{
    position:absolute;left:0;top:0;width:186px;height:50px;background:var(--white);
    display:flex;align-items:center;padding-left:16px;gap:9px;
  }
  .brand-dot{width:30px;height:30px;border-radius:50%;background:#1a1a1a;flex:none}
  .brand-name{font-size:13.5px;font-weight:600;letter-spacing:1.6px;color:#1a1a1a}
  .nav{position:absolute;left:212px;top:0;height:50px;display:flex;align-items:center;gap:15px}
  .nav a{color:var(--white);text-decoration:none;font-size:11px;font-weight:600}

  /* hero */
  .hero{position:absolute;top:50px;left:0;width:416px;height:191px}
  .hero--city{background:linear-gradient(160deg,#6f7660 0%,#a9a57a 38%,#3b4436 70%,#1f241d 100%)}
  .hero--peaks{background:linear-gradient(170deg,#7fb0ea 0%,#2f6fc8 40%,#1b56ad 70%,#174893 100%)}
  .hero-frame{
    position:absolute;left:80px;top:66px;width:255px;height:62px;
    border:1.5px solid var(--white);padding:6px;
  }
  .hero-title{
    background:var(--white);height:100%;display:flex;align-items:center;justify-content:center;
    font-size:21.5px;font-weight:900;letter-spacing:.4px;color:#000;
  }

  /* funds */
  .funds{position:absolute;top:241px;left:0;width:416px;height:217px;background:var(--ice)}
  .fund{position:absolute;top:46px;width:125px;text-align:center}
  .fund:nth-child(1){left:17px}
  .fund:nth-child(2){left:146px}
  .fund:nth-child(3){left:275px}
  .fund-photo{height:94px;border:1px solid var(--frame);padding:3px}
  .fund-photo span{display:block;width:100%;height:100%}
  .fund-name{margin-top:8px;font-size:11px;font-weight:700;line-height:13px;color:#111}
  .tone-coins{background:linear-gradient(120deg,#e6e1d8 0%,#b08a6a 45%,#7c5a44 75%,#c9c4bc 100%)}
  .tone-canada{background:linear-gradient(135deg,#f6e3e5 0%,#eef0f4 55%,#e4ebf3 100%)}
  .tone-usa{background:linear-gradient(135deg,#dfe3ee 0%,#eef0f4 50%,#f3e2e5 100%)}
  .tone-chart{background:linear-gradient(160deg,#3e6ef0 0%,#1630c8 55%,#0c1f8a 100%)}
  .tone-stack{background:linear-gradient(140deg,#f5e4d8 0%,#b8cde2 45%,#7fa6cc 80%,#e6eef7 100%)}

  /* about */
  .story{position:absolute;top:458px;left:0;width:416px;height:282px;background:var(--white)}
  .story-photo{position:absolute;left:16px;top:54px;width:149px;height:179px;border:1px solid #ddd}
  .tone-jar{background:linear-gradient(160deg,#d9e9a3 0%,#a8c46a 40%,#e3c39f 75%,#f2ede4 100%)}
  .tone-sprout{background:linear-gradient(170deg,#3f6a2e 0%,#7aa04a 40%,#8e5a3a 75%,#b6b3a6 100%)}
  .story-block{position:absolute;left:180px;width:236px}
  .story-block--about{top:55px}
  .story-block--mission{top:159px}
  .story-head{display:flex;align-items:center;gap:6px;margin-left:-1px}
  .story-icon{width:33px;height:33px;flex:none}
  .story-head h2{font-size:15.5px;font-weight:800;letter-spacing:.2px;color:#111}
  .story-block p{margin-top:5px;font-size:9.8px;line-height:13.2px;color:#222;width:236px}
  .story-rule{position:absolute;left:180px;top:146px;width:236px;height:1px;background:var(--lime)}

  /* footer */
  .footer{position:absolute;top:740px;left:0;width:416px;height:186px;background:var(--ice)}
  .footer-brand{
    position:absolute;left:16px;top:80px;display:flex;align-items:center;gap:9px;
  }
  .footer-brand .brand-name{font-size:14px}
  .contact{position:absolute;left:200px;top:0;width:216px;height:186px;background:var(--navy);color:var(--white)}
  .contact-line{position:absolute;left:20px;font-size:9.7px;font-weight:700;line-height:13px}
  .contact-line--street{top:30px}
  .contact-line--city{top:69px}
  .contact-chip{
    position:absolute;left:14px;height:20px;padding:0 6px;border:1px solid var(--white);
    display:flex;align-items:center;font-size:9.7px;font-weight:700;color:var(--white);white-space:nowrap;
  }
  .contact-chip--phone{top:103px}
  .contact-chip--toll{top:125px}
  .contact-chip--mail{top:147px}
  .legal{
    position:absolute;top:926px;left:0;width:416px;height:30px;background:var(--bar);
    display:flex;align-items:center;justify-content:center;font-size:10.4px;color:#222;
  }
</style>
</head>
<body>

<div class="variant-title" style="left:83px">EMAIL TEMPLATE-1</div>
<div class="variant-title" style="left:540px">EMAIL TEMPLATE-2</div>

<!-- Template one -->
<section class="email email--one">
  <header class="masthead">
    <div class="brand"><span class="brand-dot"></span><span class="brand-name">TARNWELL</span></div>
    <nav class="nav"><a href="#">ABOUT</a><a href="#">FUND</a><a href="#">CONTACT</a></nav>
  </header>
  <div class="hero hero--city" role="img" aria-label="Business people silhouetted in an office overlooking a city skyline">
    <div class="hero-frame"><div class="hero-title">MONTHLY REPORT</div></div>
  </div>
  <div class="funds">
    <div class="fund"><div class="fund-photo"><span class="tone-coins" role="img" aria-label="Stacked coins beside a glass jar"></span></div><div class="fund-name">OPPORTUNITIES<br>FUND</div></div>
    <div class="fund"><div class="fund-photo"><span class="tone-canada" role="img" aria-label="National flag image for the Canadian fund"></span></div><div class="fund-name">CANADIAN SMALL<br>CAP FUND</div></div>
    <div class="fund"><div class="fund-photo"><span class="tone-usa" role="img" aria-label="National flag image for the US fund"></span></div><div class="fund-name">US SMALL<br>CAP FUND</div></div>
  </div>
  <div class="story">
    <div class="story-photo tone-jar" role="img" aria-label="Hand holding a jar of coins with a seedling"></div>
    <div class="story-block story-block--about">
      <div class="story-head">
        <svg class="story-icon" viewBox="0 0 33 33"><circle cx="16.5" cy="16.5" r="15.5" fill="#fff" stroke="#a6e86a" stroke-width="1.5"/><circle cx="16.5" cy="16.5" r="8" fill="#6f8f3a"/></svg>
        <h2>ABOUT TARNWELL</h2>
      </div>
      <p>Lorem Ipsum is simply dummy text of the printing and typesetting industry. Lorem Ipsum has been the industry</p>
    </div>
    <div class="story-rule"></div>
    <div class="story-block story-block--mission">
      <div class="story-head">
        <svg class="story-icon" viewBox="0 0 33 33"><circle cx="16.5" cy="16.5" r="15.5" fill="#fff" stroke="#a6e86a" stroke-width="1.5"/><rect x="9" y="18" width="3" height="6" fill="#f0a020"/><rect x="13.5" y="15" width="3" height="9" fill="#3a8fd0"/><rect x="18" y="12" width="3" height="12" fill="#6fbf3a"/><path d="M8 16 L14 11 L18 13 L25 8" fill="none" stroke="#d03a3a" stroke-width="1.5"/></svg>
        <h2>OUR MISSION</h2>
      </div>
      <p>Lorem Ipsum is simply dummy text of the printing and typesetting industry. Lorem Ipsum has been the industry</p>
    </div>
  </div>
  <footer class="footer">
    <div class="footer-brand"><span class="brand-dot"></span><span class="brand-name">TARNWELL</span></div>
    <div class="contact">
      <div class="contact-line contact-line--street">240 ALDER QUAY WEST,<br>SUITE 1800</div>
      <div class="contact-line contact-line--city">HALDEN (ON), CANADA<br>K7M 4B2</div>
      <div class="contact-chip contact-chip--phone">PHONE: +1 (555) 310-2284</div>
      <div class="contact-chip contact-chip--toll">TOLL FREE: +1 (855) 310-2290</div>
      <div class="contact-chip contact-chip--mail">INFO@TARNWELLHOLDINGS.COM</div>
    </div>
  </footer>
  <div class="legal">©2022 by Tarnwell Holdings Inc.</div>
</section>

<!-- Template two -->
<section class="email email--two">
  <header class="masthead">
    <div class="brand"><span class="brand-dot"></span><span class="brand-name">TARNWELL</span></div>
    <nav class="nav"><a href="#">ABOUT</a><a href="#">FUND</a><a href="#">CONTACT</a></nav>
  </header>
  <div class="hero hero--peaks" role="img" aria-label="Blue-toned mountain range with clouds in the valley">
    <div class="hero-frame"><div class="hero-title">MONTHLY REPORT</div></div>
  </div>
  <div class="funds">
    <div class="fund"><div class="fund-photo"><span class="tone-coins" role="img" aria-label="Stacked coins beside a glass jar"></span></div><div class="fund-name">OPPORTUNITIES<br>FUND</div></div>
    <div class="fund"><div class="fund-photo"><span class="tone-chart" role="img" aria-label="Jar of coins over a blue market chart"></span></div><div class="fund-name">CANADIAN SMALL<br>CAP FUND</div></div>
    <div class="fund"><div class="fund-photo"><span class="tone-stack" role="img" aria-label="Stacks of coins with a soft financial graph"></span></div><div class="fund-name">US SMALL<br>CAP FUND</div></div>
  </div>
  <div class="story">
    <div class="story-photo tone-sprout" role="img" aria-label="Seedling growing from stacked coins"></div>
    <div class="story-block story-block--about">
      <div class="story-head">
        <svg class="story-icon" viewBox="0 0 33 33"><circle cx="16.5" cy="16.5" r="15.5" fill="#fff" stroke="#a6e86a" stroke-width="1.5"/><circle cx="16.5" cy="16.5" r="8" fill="#6f8f3a"/></svg>
        <h2>ABOUT TARNWELL</h2>
      </div>
      <p>Lorem Ipsum is simply dummy text of the printing and typesetting industry. Lorem Ipsum has been the industry</p>
    </div>
    <div class="story-rule"></div>
    <div class="story-block story-block--mission">
      <div class="story-head">
        <svg class="story-icon" viewBox="0 0 33 33"><circle cx="16.5" cy="16.5" r="15.5" fill="#fff" stroke="#a6e86a" stroke-width="1.5"/><rect x="9" y="18" width="3" height="6" fill="#f0a020"/><rect x="13.5" y="15" width="3" height="9" fill="#3a8fd0"/><rect x="18" y="12" width="3" height="12" fill="#6fbf3a"/><path d="M8 16 L14 11 L18 13 L25 8" fill="none" stroke="#d03a3a" stroke-width="1.5"/></svg>
        <h2>OUR MISSION</h2>
      </div>
      <p>Lorem Ipsum is simply dummy text of the printing and typesetting industry. Lorem Ipsum has been the industry</p>
    </div>
  </div>
  <footer class="footer">
    <div class="footer-brand"><span class="brand-dot"></span><span class="brand-name">TARNWELL</span></div>
    <div class="contact">
      <div class="contact-line contact-line--street">240 ALDER QUAY WEST,<br>SUITE 1800</div>
      <div class="contact-line contact-line--city">HALDEN (ON), CANADA<br>K7M 4B2</div>
      <div class="contact-chip contact-chip--phone">PHONE: +1 (555) 310-2284</div>
      <div class="contact-chip contact-chip--toll">TOLL FREE: +1 (855) 310-2290</div>
      <div class="contact-chip contact-chip--mail">INFO@TARNWELLHOLDINGS.COM</div>
    </div>
  </footer>
  <div class="legal">©2022 by Tarnwell Holdings Inc.</div>
</section>

</body>
</html>
```